Social media adds needed for our ORBITAL TONE VOYAGE @ THE BRELLMORE STARDOME

We are needing Social Media ads (IG & FB) for a Tone Soak at the Brellmore Stardome. Here is a link to the Event,
https://www.telquorivane.example/events/p/stardome-brl-48317-qmwzd
It needs to state "TOMAS ELVERING TONES presents"
"ORBITAL TONE VOYAGE @ THE BRELLMORE STARDOME" date, time and address for the event should be included, but not the price.
Saturday, August 17, 2024 7:00-8:30 pm
Location: Brellmore Stardome - 2470 Quillbrook Ave, Vancouver, BC
It needs to include a photo of the Stardome (2 options attached) and include Tomas (several photo options attached). Also attached is a photo of the show performed which could also be incorporated

```html
<!DOCTYPE html>
<html lang="en">
<head>
<meta charset="utf-8">
<title>Orbital Tone Voyage — Social Ad</title>
<link rel="stylesheet" href="https://fonts.googleapis.com/css2?family=Poppins:wght@400;600;700;800&display=swap">
<style>
  :root {
    --navy: #0c0a7e;
    --ink: #0a0a0a;
    --orange: #e8750a;
    --panel-deep: #0a1560;
    --panel-bright: #1a2fb0;
    --white: #ffffff;
  }
  * { margin: 0; padding: 0; box-sizing: border-box; }
  html, body { width: 1200px; height: 1200px; overflow: hidden; background: #ffffff; }
  .ad {
    position: relative; width: 1200px; height: 1200px; overflow: hidden;
    font-family: "Poppins", sans-serif; color: var(--ink);
    background: linear-gradient(180deg, #ffffff 0%, #ffffff 30%, #eeeeee 48%, #f6f6f6 58%, #e4e4e4 70%, #ffffff 100%);
  }
  .venue-panel {
    position: absolute; left: 875px; top: 0; width: 325px; height: 1200px;
    background:
      radial-gradient(circle at 50% 54%, #f08a1a 0 4%, #b8521a 8%, rgba(30,40,130,0.9) 20%, transparent 32%),
      radial-gradient(circle at 50% 21%, #070f48 0 40%, transparent 41%),
      linear-gradient(180deg, var(--panel-deep) 0%, #1424a0 45%, var(--panel-bright) 60%, #0d1a80 100%);
  }
  .pin { position: absolute; left: 999px; top: 62px; }
  .venue-name {
    position: absolute; left: 917px; top: 154px; color: var(--orange);
    font-weight: 700; font-size: 29px; line-height: 40px;
  }
  .venue-address {
    position: absolute; left: 917px; top: 240px; color: var(--white);
    font-weight: 700; font-size: 29px; line-height: 39px;
  }
  .presenter { position: absolute; left: 84px; top: 58px; font-weight: 800; font-size: 54px; letter-spacing: 0.3px; }
  .presents { position: absolute; left: 84px; top: 133px; font-weight: 400; font-size: 43px; letter-spacing: 19px; }
  .title-main { position: absolute; left: 80px; top: 186px; color: var(--navy); font-weight: 800; font-size: 146px; line-height: 1.2; letter-spacing: -2px; }
  .title-sub { position: absolute; left: 84px; top: 336px; color: var(--orange); font-weight: 800; font-size: 82px; line-height: 1.2; }
  .rule { position: absolute; left: 84px; width: 707px; height: 3px; background: #10123a; }
  .rule-top { top: 440px; } .rule-bottom { top: 524px; }
  .venue-line { position: absolute; left: 84px; top: 455px; font-weight: 800; font-size: 45px; }
  .day-number { position: absolute; left: 86px; top: 558px; color: var(--navy); font-weight: 600; font-size: 112px; line-height: 1.1; letter-spacing: -4px; }
  .month { position: absolute; left: 180px; top: 568px; font-weight: 800; font-size: 49px; line-height: 1.1; }
  .weekday { position: absolute; left: 180px; top: 616px; font-weight: 400; font-size: 41px; line-height: 1.1; }
  .year-tag {
    position: absolute; left: 412px; top: 577px; width: 29px; height: 82px; background: var(--navy);
    color: var(--white); font-size: 21px; font-weight: 400;
    display: flex; align-items: center; justify-content: center;
  }
  .year-tag span { transform: rotate(-90deg); white-space: nowrap; }
  .date-label { position: absolute; left: 464px; top: 566px; color: var(--navy); font-weight: 800; font-size: 48px; line-height: 1.1; }
  .time { position: absolute; left: 464px; top: 614px; font-weight: 400; font-size: 52px; line-height: 1.1; }
  .stardome-photo {
    position: absolute; left: 0; top: 720px; width: 875px; height: 480px;
    background:
      radial-gradient(ellipse 40% 45% at 38% 72%, #cfe3dc 0%, #9fbdb4 40%, rgba(120,140,135,0) 100%),
      radial-gradient(ellipse 30% 18% at 60% 12%, rgba(255,255,255,0.95), rgba(255,255,255,0) 100%),
      linear-gradient(180deg, rgba(240,240,240,0) 0%, #8a8a8a 14%, #5a5a5a 40%, #6e6e6e 70%, #3a3f3e 100%);
  }
  .bowls-photo {
    position: absolute; left: 560px; top: 1040px; width: 230px; height: 160px;
    border-radius: 18px 18px 0 0;
    background: linear-gradient(180deg, #f1ecea 0%, #d9d4cf 55%, #aeb2aa 100%);
  }
  .performer-photo {
    position: absolute; left: 735px; top: 685px; width: 440px; height: 515px;
    border-radius: 220px 220px 0 0;
    background: linear-gradient(180deg, rgba(60,60,90,0.0) 0%, #3a3550 14%, #cfcfe0 30%, #f2f2f7 60%, #e6e6ef 100%);
  }
</style>
</head>
<body>
<main class="ad">
  <div class="venue-panel" role="img" aria-label="Deep blue photo of gongs glowing in a dark room, one lit by an orange glow"></div>
  <div class="stardome-photo" role="img" aria-label="Photo of the domed stardome building lit at dusk with a crab sculpture in front and grey hills behind"></div>
  <div class="performer-photo" role="img" aria-label="Photo of the sound artist in white seated cross-legged, raising a wind chime"></div>
  <div class="bowls-photo" role="img" aria-label="Photo of frosted crystal singing bowls in front of the artist"></div>

  <svg class="pin" width="68" height="68" viewBox="0 0 68 68" aria-hidden="true">
    <circle cx="34" cy="34" r="34" fill="#e8750a"/>
    <path d="M34 16c-8 0-14 6-14 14 0 10 14 23 14 23s14-13 14-23c0-8-6-14-14-14z" fill="#fff"/>
    <circle cx="34" cy="30" r="5" fill="#e8750a"/>
  </svg>
  <p class="venue-name">BRELLMORE<br>STARDOME</p>
  <p class="venue-address">2470<br>Quillbrook Ave,<br>Vancouver,<br>BC</p>

  <h2 class="presenter">TOMAS ELVERING TONES</h2>
  <p class="presents">PRESENTS</p>
  <h1 class="title-main">ORBITAL</h1>
  <p class="title-sub">TONE VOYAGE</p>
  <div class="rule rule-top"></div>
  <p class="venue-line">THE BRELLMORE STARDOME</p>
  <div class="rule rule-bottom"></div>

  <p class="day-number">17</p>
  <p class="month">AUGUST</p>
  <p class="weekday">SATURDAY</p>
  <div class="year-tag"><span>2024</span></div>
  <p class="date-label">DATE</p>
  <p class="time">7:00-8:30 PM</p>
</main>
</body>
</html>
```